Bold Website Design for Fitness Trainer - No Coding

We are in need of a bold and unique website design for a personal fitness training company, www.TessaLorvel.com. We need DESIGN ONLY for three pages. These will be a homepage, a lead capture page, and one internal page with a sidebar. The design will be used for coding a wordpress theme, if that matters for the designer.

Tessa Lorvel Fitness Training
2738 E 19th St #415
Austin, TX 78705
512-607-4918
http://www.tessalorvel.com

Target Market(s)

18-45 year old male and females making 80k+ a year and looking to get stronger and in shape.

Industry/Entity Type

Fitness

Number of Pages Required

3 page

Font styles to use
Sans Serif

Requirements
Must have
• See attached design specs file.
Nice to have
Should not have
• Boxed layout.
• Dark Background.

```html
<!DOCTYPE html>
<html lang="en">
<head>
<meta charset="utf-8">
<title>Tessa Lorvel Fitness Training</title>
<link rel="stylesheet" href="https://fonts.googleapis.com/css2?family=Montserrat:wght@400;600;700;800&display=swap">
<style>
:root{
  --cyan:#1fb8e6;
  --cyan-deep:#12a7d3;
  --magenta:#c2267f;
  --pink:#d33a8e;
  --yellow:#ffe21a;
  --mustard:#c9b400;
  --purple:#4b36a8;
  --night:#2d2870;
  --ink:#0d0d0d;
  --white:#ffffff;
}
*{box-sizing:border-box;margin:0;padding:0}
html,body{width:1200px;height:3046px;overflow:hidden}
body{font-family:"Montserrat",Arial,sans-serif;color:var(--white);background:var(--white);position:relative}
.abs{position:absolute}

/* top bar */
.topbar{left:0;top:0;width:1200px;height:41px;background:var(--cyan);font-size:12px;font-weight:600}
.topbar .contact{left:112px;top:13px;display:flex;gap:22px}
.topbar .contact span{display:flex;align-items:center;gap:7px}
.topbar .social{right:112px;top:7px;display:flex;gap:9px}
.dot{width:27px;height:27px;border-radius:50%;background:var(--white)}

/* header */
.header{left:0;top:41px;width:1200px;height:121px;background:var(--white)}
.brand{left:444px;top:22px;display:flex;align-items:center;gap:14px}
.brand .mark{width:76px;height:76px;border-radius:50%;background:var(--yellow)}
.brand .name{font-size:38px;font-weight:800;color:var(--ink);line-height:1}

/* hero */
.hero{left:0;top:162px;width:1200px;height:674px;background:linear-gradient(100deg,#b21f76 0%,#cf3b90 55%,#b52379 100%)}
.nav{left:0;top:185px;width:1200px;height:30px;font-size:12px;font-weight:700;letter-spacing:.5px}
.nav a{position:absolute;transform:translateX(-50%);color:var(--white);text-decoration:none;white-space:nowrap}
.nav .active:after{content:"";position:absolute;left:-8px;right:-8px;top:22px;height:3px;background:var(--yellow)}
.hero-kicker{left:106px;top:452px;font-size:32px;font-weight:800;color:var(--yellow)}
.hero-title{left:106px;top:500px;font-size:50px;font-weight:800;line-height:66px}
.hero-btn{left:112px;top:680px;width:280px;height:51px;border:2px solid var(--white);border-radius:26px;font-size:15px;font-weight:700;display:flex;align-items:center;justify-content:center;letter-spacing:.5px}
.arrow{width:22px;height:40px}

/* services */
.services{left:0;top:836px;width:1200px;height:581px;background:radial-gradient(ellipse at 55% 50%,#3a3a3a 0%,#141414 55%,#050505 100%)}
.section-title{width:1200px;text-align:center;font-weight:800;letter-spacing:1px}
.svc-row{left:112px;top:1007px;width:974px;height:293px;display:flex;background:var(--mustard)}
.svc{flex:1;display:flex;flex-direction:column;align-items:center;padding-top:58px;font-size:19px;font-weight:600;text-align:center}
.svc.featured{flex:0 0 243px;background:var(--cyan)}
.svc svg{width:72px;height:72px;margin-bottom:26px}
.svc .rule{width:46px;height:2px;background:var(--white);margin:14px 0 10px}
.svc p{font-size:11px;line-height:18px;padding:0 22px;font-weight:400}

/* testimonials */
.testimonials{left:0;top:1417px;width:1200px;height:373px;background:linear-gradient(90deg,#c42b80,#dd4f9c 50%,#c42b80)}
.quote{width:1200px;text-align:center;font-size:15px;font-weight:600;line-height:22px}
.author{width:1200px;text-align:center;font-size:15px;font-style:italic}

/* connect */
.connect{left:0;top:1790px;width:1200px;height:321px;background:var(--cyan-deep)}
.stats{left:112px;top:1924px;display:flex;gap:28px}
.stat{width:224px;height:130px;background:rgba(255,255,255,.13);display:flex;align-items:center;padding-left:24px;gap:24px}
.stat .dot{width:38px;height:38px;background:rgba(255,255,255,.9)}
.stat b{display:block;font-size:30px;font-weight:700;padding-bottom:4px;border-bottom:2px solid var(--white);width:max-content}
.stat span{display:block;font-size:15px;padding-top:5px}

/* blog */
.blog{left:0;top:2111px;width:1200px;height:686px;background:radial-gradient(ellipse at 60% 45%,#5641b8 0%,#4530a0 60%,#3a2790 100%)}
.post{left:387px;width:560px;height:130px}
.post .thumb{position:absolute;left:0;top:0;width:140px;height:94px}
.post .text{position:absolute;left:250px;top:0}
.post small{font-size:12px;font-weight:700;letter-spacing:1px}
.post h3{font-size:24px;font-weight:700;letter-spacing:1px;margin:4px 0 10px}
.post p{font-size:12px;line-height:24px;width:300px}
.post .line{position:absolute;left:250px;top:150px;width:310px;height:1px;background:rgba(255,255,255,.2)}

/* footer */
.footer{left:0;top:2797px;width:1200px;height:203px;background:var(--night);font-size:11px}
.footer .dot{width:26px;height:26px;background:#1c1a45;border:1px solid #555}
.signup{left:914px;top:2915px;width:146px;height:28px;border:1px solid var(--white);border-radius:14px;font-size:10px;padding:8px 12px}
.footbar{left:0;top:3000px;width:1200px;height:46px;background:#ffd800}
</style>
</head>
<body>

<div class="abs topbar">
  <div class="abs contact">
    <span><svg width="12" height="12" viewBox="0 0 24 24"><path fill="#fff" d="M6.6 10.8a15 15 0 0 0 6.6 6.6l2.2-2.2c.3-.3.7-.4 1-.2 1.1.4 2.3.6 3.6.6.6 0 1 .4 1 1V20c0 .6-.4 1-1 1A17 17 0 0 1 3 4c0-.6.4-1 1-1h3.5c.6 0 1 .4 1 1 0 1.3.2 2.5.6 3.6.1.3 0 .7-.2 1z"/></svg>(512) 607-4918</span>
    <span><svg width="10" height="13" viewBox="0 0 20 26"><path fill="#fff" d="M10 0a10 10 0 0 0-10 10c0 7.5 10 16 10 16s10-8.5 10-16A10 10 0 0 0 10 0zm0 14a4 4 0 1 1 0-8 4 4 0 0 1 0 8z"/></svg>2738 E 19th St #415, Austin, TX 78705</span>
    <span><svg width="13" height="10" viewBox="0 0 26 20"><rect width="26" height="20" rx="2" fill="#fff"/><path d="M1 2l12 9 12-9" stroke="#1fb8e6" stroke-width="2" fill="none"/></svg>hello@tessalorvel.com</span>
  </div>
  <div class="abs social"><i class="dot"></i><i class="dot"></i><i class="dot"></i><i class="dot"></i></div>
</div>

<header class="abs header">
  <div class="abs brand"><span class="mark"></span><span class="name">Tessa Lorvel</span></div>
</header>

<section class="abs hero" role="img" aria-label="Photo of the trainer in boxing gloves throwing a punch, magenta toned"></section>
<nav class="abs nav">
  <a class="active" style="left:203px">HOME</a>
  <a style="left:313px">PROGRAMS</a>
  <a style="left:493px">MEET YOUR TRAINER</a>
  <a style="left:652px">BLOG</a>
  <a style="left:798px">CONTACT ME</a>
  <a style="left:960px">FREE SESSION</a>
</nav>
<svg class="abs arrow" style="left:60px;top:514px" viewBox="0 0 22 40"><path d="M18 4L4 20l14 16" stroke="#fff" stroke-width="2.5" fill="none"/></svg>
<svg class="abs arrow" style="left:1110px;top:514px" viewBox="0 0 22 40"><path d="M4 4l14 16L4 36" stroke="#fff" stroke-width="2.5" fill="none"/></svg>
<div class="abs hero-kicker">GET STARTED TODAY</div>
<h1 class="abs hero-title">YOUR FIRST<br>SESSIONS IS FREE!</h1>
<div class="abs hero-btn">APPOINTMENT WITH TESSA</div>

<section class="abs services" role="img" aria-label="Dark photo of barbell weight plates on a gym floor"></section>
<h2 class="abs section-title" style="top:902px;font-size:30px">MY SERVICES</h2>
<div class="abs svc-row">
  <div class="svc featured">
    <svg viewBox="0 0 72 72"><g stroke="#fff" stroke-width="4" fill="none" stroke-linecap="round"><path d="M16 40l16-16 8 8-16 16z"/><path d="M32 48l16-16 8 8-16 16z"/><path d="M36 28l8-8"/></g></svg>
    GENERAL FITNESS
    <span class="rule"></span>
    <p>Lorem ipsum dolor sit amet cons ectetur adipiscing elit. Nunc sit amet pulvinar nulla, quis facilisis nulla.</p>
  </div>
  <div class="svc">
    <svg viewBox="0 0 72 72"><g stroke="#fff" stroke-width="4" fill="none"><circle cx="36" cy="40" r="24"/><path d="M36 40V26M30 8h12M36 8v8"/></g></svg>
    WEIGHT LOSS<span class="rule"></span>
  </div>
  <div class="svc">
    <svg viewBox="0 0 72 72"><g fill="#fff"><rect x="4" y="30" width="64" height="6"/><rect x="12" y="20" width="7" height="26"/><rect x="21" y="16" width="7" height="34"/><rect x="44" y="16" width="7" height="34"/><rect x="53" y="20" width="7" height="26"/></g></svg>
    STRENGTH TRAINING<span class="rule"></span>
  </div>
  <div class="svc">
    <svg viewBox="0 0 72 72"><path fill="#fff" d="M24 8h24a8 8 0 0 1 8 8v8l-4 4a26 26 0 1 1-32 0l-4-4v-8a8 8 0 0 1 8-8zm2 8v8h20v-8z"/></svg>
    POWERLIFTING<span class="rule"></span>
  </div>
</div>

<section class="abs testimonials" role="img" aria-label="Photo of athletes' torsos, pink toned"></section>
<svg class="abs arrow" style="left:88px;top:1588px" viewBox="0 0 22 40"><path d="M18 4L4 20l14 16" stroke="#fff" stroke-width="2.5" fill="none"/></svg>
<svg class="abs arrow" style="left:1080px;top:1588px" viewBox="0 0 22 40"><path d="M4 4l14 16L4 36" stroke="#fff" stroke-width="2.5" fill="none"/></svg>
<h2 class="abs section-title" style="top:1555px;font-size:28px">TESTIMONIALS</h2>
<p class="abs quote" style="top:1620px">«I enjoy the encouragement from the Tessa. The environment is always<br>super positive and fun.»</p>
<p class="abs author" style="top:1675px">Marcus Ellery</p>

<section class="abs connect"></section>
<h2 class="abs section-title" style="top:1842px;font-size:27px">CONNECT WITH ME</h2>
<div class="abs stats">
  <div class="stat"><i class="dot"></i><div><b>3362</b><span>Likes</span></div></div>
  <div class="stat"><i class="dot"></i><div><b>153</b><span>Followers</span></div></div>
  <div class="stat"><i class="dot"></i><div><b>89</b><span>Videos</span></div></div>
  <div class="stat"><i class="dot"></i><div><b>2,998</b><span>Followers</span></div></div>
</div>

<section class="abs blog" role="img" aria-label="Blurred photo of a gym interior, purple toned"></section>
<h2 class="abs section-title" style="top:2196px;font-size:29px">WELCOME TO MY BLOG</h2>
<article class="abs post" style="top:2272px">
  <div class="thumb" style="background:linear-gradient(90deg,#3aa6c8,#8c3a78)" role="img" aria-label="Photo from a fitness event"></div>
  <div class="text"><small>FITNESS</small><h3>AUSTIN EVENT</h3><p>Consectetur adipiscing elit. Nunc sit amet pulvinar nulla, quis facilisis nulla.</p></div>
  <span class="line"></span>
</article>
<article class="abs post" style="top:2440px">
  <div class="thumb" style="background:linear-gradient(90deg,#d8a890,#8a5a48)" role="img" aria-label="Photo of the trainer flexing"></div>
  <div class="text"><small>BOXING</small><h3>FITNESS EVENT</h3><p>Consectetur adipiscing elit. Nunc sit amet pulvinar nulla, quis facilisis nulla.</p></div>
  <span class="line"></span>
</article>
<article class="abs post" style="top:2608px">
  <div class="thumb" style="background:linear-gradient(90deg,#b8c4cc,#7a6a60)" role="img" aria-label="Photo of the trainer in a headscarf"></div>
  <div class="text"><small>SECRETS</small><h3>WEIGHT LOST</h3><p>Consectetur adipiscing elit. Nunc sit amet pulvinar nulla, quis facilisis nulla.</p></div>
</article>
<svg class="abs" style="left:586px;top:2756px" width="28" height="16" viewBox="0 0 28 16"><path d="M2 2l12 12L26 2" stroke="#fff" stroke-width="2.5" fill="none"/></svg>

<footer class="abs footer">
  <p class="abs" style="left:112px;top:70px">Copyright 2015 <span style="color:var(--pink)">Tessa Lorvel</span></p>
  <div class="abs" style="left:112px;top:122px;display:flex;gap:10px"><i class="dot"></i><i class="dot"></i><i class="dot"></i><i class="dot"></i></div>
  <p class="abs" style="left:440px;top:70px;width:320px;text-align:center;line-height:20px">Tessa Lorvel Fitness Training<br>2738 E 19th St #415<br>Austin, TX 78705<br>(512) 607-4918</p>
  <p class="abs" style="left:918px;top:70px;color:var(--pink);font-weight:700">Keep in touch</p>
</footer>
<div class="abs signup">Your email<svg style="position:absolute;right:10px;top:8px" width="10" height="10" viewBox="0 0 10 10"><path d="M0 5h8M5 1l4 4-4 4" stroke="#fff" stroke-width="2" fill="none"/></svg></div>
<div class="abs footbar"></div>

</body>
</html>
```